Artist business cards needed, happy acrylic painter

I'd like a business card I can hand out to people interested in my paintings. I'd like a logo that includes elements of my painting. I have shared a collection that may be used at https://qlvbox.example/albums/7TrpWdKz3mNa8bQeXy
I get my vibe and the type of art I create, you can also see my active Vornet Circle account: https://circle.vornetso.example/+MirelaQuade

Target Market(s)

people interested in art

Industry/Entity Type

Artists

Contact Information for Business Card

Mirela Quade
555-014-7392
mirelaquade@postvale.example
mirelaquade@postvale.example
www.mirelaquade.example

Font styles to use
Sans Serif
Decorative
Script

Requirements
Must have
• 1. Colors that are represented in my paintings
• 2. Elements from my paintings: Link to the vornet locker with my art: https://qlvbox.example/albums/7TrpWdKz3mNa8bQeXy
• 3. Flower(s)
• 4. A box on the back that's outlined so a note could be added. I've attached a photo of a business card my friend uses for her floral design company as an example of the back of the card with the quote and a box and business name (Mirela Quade).
• 4. I'd like to have this quote on the back of the card too.
• "I must have flowers, always and always."
• ~Tobiah Varnsell
Nice to have
• In smaller font
• If it fits, links to my other social media:
• https://circle.vornetso.example/+MirelaQuade
• https://www.friendlane.example/mirelaquadeartist/
Should not have
• A dark background

```html
<!DOCTYPE html>
<html lang="en">
<head>
<meta charset="utf-8">
<title>Mirela Quade – Business Card</title>
<link rel="stylesheet" href="https://fonts.googleapis.com/css2?family=Arimo:wght@400;700&family=Pinyon+Script&display=swap">
<style>
  :root {
    --page: #ffffff;
    --cream: #efeee0;
    --lavender: #a991cf;
    --violet: #8f86d4;
    --magenta: #c568a6;
    --leaf: #a9c79a;
    --ink: #5a5a5a;
    --plum: #7a5a8c;
    --plum-line: #9b72a8;
    --social-a: #3b5a9a;
    --social-b: #dd4b39;
  }
  * { margin: 0; padding: 0; box-sizing: border-box; }
  html, body { width: 1200px; height: 1000px; overflow: hidden; background: var(--page); }
  body { position: relative; font-family: "Arimo", Arial, sans-serif; }

  .card { position: absolute; left: 271px; width: 658px; height: 376px; overflow: hidden; }
  .card--front { top: 114px; }
  .card--back { top: 510px; }

  .painting { position: absolute; inset: 0; }
  .card--front .painting {
    background:
      radial-gradient(ellipse 120px 70px at 420px 280px, rgba(197,104,166,.55), transparent 70%),
      radial-gradient(ellipse 110px 60px at 570px 250px, rgba(143,134,212,.7), transparent 70%),
      radial-gradient(ellipse 160px 110px at 520px 340px, rgba(169,145,207,.8), transparent 75%),
      radial-gradient(ellipse 150px 90px at 600px 120px, rgba(169,145,207,.75), transparent 75%),
      radial-gradient(ellipse 90px 60px at 470px 40px, rgba(169,199,154,.45), transparent 75%),
      linear-gradient(90deg, var(--cream) 0%, #ece7df 45%, #d9cde3 70%, #b9a8dc 100%);
  }
  .card--back .painting {
    background:
      radial-gradient(ellipse 80px 120px at 640px 90px, rgba(143,134,212,.8), transparent 75%),
      radial-gradient(ellipse 80px 140px at 650px 300px, rgba(143,134,212,.8), transparent 75%),
      radial-gradient(ellipse 140px 90px at 120px 320px, rgba(212,180,220,.5), transparent 75%),
      radial-gradient(ellipse 120px 80px at 150px 150px, rgba(169,199,154,.3), transparent 75%),
      linear-gradient(90deg, var(--cream) 0%, #ece6e0 50%, #d6c8e2 80%, #a99ad6 100%);
  }

  .name {
    position: absolute; left: 20px; top: 48px;
    font-family: "Pinyon Script", cursive; font-weight: 400;
    font-size: 62px; color: var(--plum); white-space: nowrap;
  }
  .contact { position: absolute; left: 36px; top: 185px; font-size: 22px; line-height: 30px; color: var(--ink); }
  .contact .web { color: var(--plum); font-weight: 700; }
  .social { position: absolute; left: 36px; display: flex; align-items: center; gap: 8px; font-size: 18px; }
  .social .mark { width: 30px; height: 30px; }
  .social--friendlane { top: 290px; color: var(--social-a); }
  .social--friendlane .mark { background: var(--social-a); }
  .social--circle { top: 332px; color: var(--social-b); }
  .social--circle .mark { background: var(--social-b); }

  .notes-box {
    position: absolute; left: 243px; top: 27px; width: 393px; height: 321px;
    background: #fff; border: 5px solid var(--plum-line);
    border-radius: 8px 62px 8px 62px;
  }
  .notes-label { position: absolute; left: 18px; top: 18px; font-size: 14px; color: var(--plum); }
  .quote { position: absolute; left: 36px; top: 266px; font-size: 20px; line-height: 27px; color: var(--ink); }
  .attribution { position: absolute; left: 36px; top: 341px; font-size: 15px; color: var(--ink); }
</style>
</head>
<body>
  <section class="card card--front">
    <div class="painting" role="img" aria-label="Textured acrylic painting of lavender and pink flowers fading into cream"></div>
    <h1 class="name">Mirela Quade</h1>
    <div class="contact">
      <p>555-014-7392</p>
      <p>mirelaquade@postvale.example</p>
      <p class="web">www.mirelaquade.example</p>
    </div>
    <p class="social social--friendlane"><span class="mark"></span>Friendlane /mirelaquadeartist</p>
    <p class="social social--circle"><span class="mark"></span>Vornet Circle /+MirelaQuade</p>
  </section>

  <section class="card card--back">
    <div class="painting" role="img" aria-label="Soft acrylic painting of pale flowers with violet blooms at the edge"></div>
    <p class="quote">"I must have flowers,<br>always and always."</p>
    <p class="attribution">- Tobiah Varnsell</p>
    <div class="notes-box"><span class="notes-label">NOTES</span></div>
  </section>
</body>
</html>
```